Web design for Modeling agency

We are looking for re-designing our modeling agency website.
Current website: lunafaces.com our competitor: KTRfaces.com
http://brisaface.fr/
https://www.corvelmanagement.com/models/
https://www.hedwig-faces.de
https://www.rustmanagement.co.uk
https://www.quorbfaces.com
https://www.harborlightfaces.com

Target Market(s)

modeling agency

Industry/Entity Type

modeling agency

Number of Pages Required

5+ page

Font styles to use
Other font styles liked:
• base on logo guidline

Requirements
Nice to have
• current website: lunafaces.com our competitor: KTRfaces.com

```html
<!DOCTYPE html>
<html lang="en">
<head>
<meta charset="UTF-8">
<title>Luna Model Agency – Choose</title>
<link rel="stylesheet" href="https://fonts.googleapis.com/css2?family=Cormorant+Garamond:wght@400;500&family=Questrial&display=swap">
<style>
  :root {
    --bg-deep: #050505;
    --bg-soft: #151311;
    --tan: #b9977e;
    --tan-text: #c4a086;
    --white: #ffffff;
    --nav-grey: #3a3a3a;
    --footer-grey: #8d8d8d;
    --rule: #4a4a4a;
  }
  * { margin: 0; padding: 0; box-sizing: border-box; }
  html, body { width: 1200px; height: 2740px; overflow: hidden; }
  body {
    position: relative;
    background: radial-gradient(ellipse at 55% 35%, var(--bg-soft) 0%, var(--bg-deep) 70%);
    font-family: "Questrial", sans-serif;
    color: var(--white);
  }
  .top-ticker {
    position: absolute; top: 158px; left: 0; width: 1200px; height: 70px;
    white-space: nowrap; overflow: hidden;
    font-size: 56px; color: var(--nav-grey);
  }
  .top-ticker span { position: absolute; top: 0; }
  .brand-name-block {
    position: absolute; top: 560px; left: 0; width: 1200px; height: 320px;
    text-align: center;
    font-family: "Questrial", sans-serif; font-weight: 400;
    font-size: 280px; line-height: 320px;
    color: var(--tan);
  }
  .city-row {
    position: absolute; left: 0; width: 1200px; height: 60px;
    font-size: 55px; letter-spacing: 1px; color: var(--white);
  }
  .city-row span { position: absolute; top: 0; line-height: 60px; }
  .city-row .dot {
    width: 20px; height: 20px; background: var(--tan);
    transform: rotate(45deg); top: 22px;
  }
  .choose-title {
    position: absolute; top: 1395px; left: 0; width: 1200px; text-align: center;
    font-family: "Cormorant Garamond", serif; font-weight: 400;
    font-size: 126px; line-height: 137px; letter-spacing: 20px;
    color: var(--tan-text); text-transform: uppercase;
  }
  .choice {
    position: absolute; left: 263px; width: 674px; height: 163px;
    display: flex; align-items: center; justify-content: center;
    font-size: 58px; letter-spacing: 9px; text-transform: uppercase;
    text-decoration: none;
  }
  .choice--women { top: 1780px; background: var(--tan); color: var(--white); }
  .choice--men { top: 1980px; border: 3px solid var(--tan); color: var(--tan-text); }
  .footer-rule {
    position: absolute; top: 2462px; left: 0; width: 1200px; height: 3px; background: var(--rule);
  }
  .footer-note {
    position: absolute; top: 2568px; left: 0; width: 1200px; text-align: center;
    font-size: 49px; color: var(--footer-grey);
  }
  .footer-note .brand-name { color: var(--tan-text); }
</style>
</head>
<body>
  <nav class="top-ticker" aria-label="Agency sections">
    <span style="left:-60px">Men</span>
    <span style="left:277px">In Town</span>
    <span style="left:677px">Luna Mother Agency</span>
  </nav>

  <div class="brand-name-block">LUNA</div>

  <div class="city-row" style="top:993px">
    <span style="left:118px">LONDON</span>
    <span class="dot" style="left:402px"></span>
    <span style="left:492px">PARIS</span>
    <span class="dot" style="left:750px"></span>
    <span style="left:798px">ISTANBUL</span>
  </div>
  <div class="city-row" style="top:1110px">
    <span style="left:170px">MILAN</span>
    <span class="dot" style="left:402px"></span>
    <span style="left:484px">ATHENS</span>
    <span class="dot" style="left:803px"></span>
    <span style="left:848px">DUBAI</span>
  </div>

  <h1 class="choose-title">Choosing<br>Modal</h1>

  <a class="choice choice--women" href="#women">Women</a>
  <a class="choice choice--men" href="#men">Men</a>

  <div class="footer-rule"></div>
  <footer class="footer-note">© 2021 <span class="brand-name">Luna Model Agency</span> All right reserved</footer>
</body>
</html>
```